Packaging for New Supplement Line

Need a cool, military themed package designed for new supplement line inspired by a retired Navy Seal. Maybe use KDL Grade V camo (example attached) as background and military fonts - just a suggestion maybe you have a way cooler idea? Product name is "ZKRT Iron Vanguard"
Navy Seal has a logo we'd like featured somewhere small or not "loud" on the package (example attached) Product to be packaged in a "wide mouth" pouch (example attached) but want a small window to view the contents. Contents will be a special vanilla protein powder in clear stickpacks (example attached) The design should reflect military strength cutting edge, superior nutrition.

```html
<!DOCTYPE html>
<html lang="en">
<head>
<meta charset="utf-8">
<title>ZKRT Iron Vanguard Whey Protein – Pouch Front</title>
<link href="https://fonts.googleapis.com/css2?family=Black+Ops+One&family=Chakra+Petch:wght@600;700&display=swap" rel="stylesheet">
<style>
  :root {
    --page: #ffffff;
    --sand-light: #e8d9bb;
    --sand-mid: #cdb38d;
    --camo-tan: #c2a47c;
    --camo-brown: #8f6c47;
    --earth-dark: #6b4d30;
    --earth-mid: #a68763;
    --trim: #b89a72;
    --window: #6a4b2e;
  }
  html, body {
    margin: 0;
    width: 1200px;
    height: 750px;
    overflow: hidden;
    background: var(--page);
  }
  .pouch-front {
    position: absolute;
    left: 100px;
    top: 32px;
    width: 1000px;
    height: 685px;
    background: var(--sand-light);
    overflow: hidden;
  }
  .camo-art {
    position: absolute;
    inset: 0;
  }
  .base-band {
    position: absolute;
    left: 0; right: 0; bottom: 0;
    height: 8px;
    background: var(--earth-dark);
  }
  .affiliation {
    position: absolute;
    left: 455px;
    top: 282px;
    display: flex;
    align-items: center;
    gap: 8px;
  }
  .affiliation-dot {
    width: 34px;
    height: 34px;
    border-radius: 50%;
    border: 2px solid var(--earth-mid);
    box-sizing: border-box;
  }
  .affiliation-name {
    font-family: "Chakra Petch", sans-serif;
    font-weight: 700;
    font-size: 12px;
    letter-spacing: 1px;
    color: var(--earth-mid);
  }
  .brand-mark {
    position: absolute;
    left: 67px;
    top: 343px;
    width: 360px;
    text-align: center;
  }
  .brand-name {
    font-family: "Black Ops One", sans-serif;
    font-size: 84px;
    line-height: 84px;
    color: var(--earth-dark);
    letter-spacing: 4px;
  }
  .brand-tagline {
    margin-top: 2px;
    background: var(--earth-mid);
    color: var(--sand-light);
    font-family: "Black Ops One", sans-serif;
    font-size: 20px;
    line-height: 24px;
    letter-spacing: 5px;
  }
  .product-title {
    position: absolute;
    right: 38px;
    top: 312px;
    text-align: right;
    font-family: "Black Ops One", sans-serif;
  }
  .flavour {
    font-family: "Chakra Petch", sans-serif;
    font-weight: 700;
    font-size: 17px;
    color: var(--earth-dark);
    letter-spacing: 0.5px;
  }
  .title-whey {
    font-size: 76px;
    line-height: 66px;
    color: var(--earth-dark);
    letter-spacing: 4px;
    margin-top: 4px;
  }
  .title-protein {
    font-size: 76px;
    line-height: 66px;
    color: var(--earth-mid);
    letter-spacing: 4px;
  }
  .view-window {
    position: absolute;
    left: 47px;
    top: 477px;
    width: 373px;
    height: 159px;
    border-radius: 30px;
    background: var(--window);
  }
  .benefits {
    position: absolute;
    left: 470px;
    top: 536px;
    width: 495px;
    display: flex;
    font-family: "Chakra Petch", sans-serif;
    font-weight: 700;
    font-size: 14px;
    line-height: 15px;
    color: var(--earth-dark);
    text-align: center;
  }
  .benefit {
    padding: 4px 0;
  }
  .benefit + .benefit {
    border-left: 2px solid var(--earth-mid);
  }
  .benefit:nth-child(1) { width: 135px; }
  .benefit:nth-child(2) { width: 180px; }
  .benefit:nth-child(3) { width: 180px; }
  .benefit-rule {
    position: absolute;
    left: 473px;
    top: 582px;
    width: 465px;
    height: 2px;
    background: var(--earth-mid);
  }
  .net-contents {
    position: absolute;
    left: 473px;
    top: 594px;
    width: 465px;
    text-align: center;
    font-family: "Chakra Petch", sans-serif;
    font-weight: 700;
    font-size: 14px;
    color: var(--earth-dark);
  }
</style>
</head>
<body>
  <main class="pouch-front">
    <svg class="camo-art" width="1000" height="685" viewBox="0 0 1000 685" role="img" aria-label="KDL Grade V digital desert camouflage pattern across the top of the pouch">
      <defs>
        <linearGradient id="camoTone" x1="0" y1="0" x2="1" y2="1">
          <stop offset="0" stop-color="#c9ad86"/>
          <stop offset="0.5" stop-color="#b8966c"/>
          <stop offset="1" stop-color="#c6a982"/>
        </linearGradient>
      </defs>
      <path d="M0 0 H1000 V189 H600 C520 189 470 215 430 260 C395 300 360 317 300 317 H0 Z" fill="url(#camoTone)"/>
      <path d="M0 319 H300 C360 319 397 302 432 262 C472 217 522 191 600 191 H1000" fill="none" stroke="var(--trim)" stroke-width="5"/>
    </svg>

    <div class="affiliation">
      <span class="affiliation-dot"></span>
      <span class="affiliation-name">TIDEWATER CORPS</span>
    </div>

    <div class="brand-mark">
      <div class="brand-name">ZKRT</div>
      <div class="brand-tagline">IRON VANGUARD</div>
    </div>

    <div class="product-title">
      <div class="flavour">NATURAL VANILLA FLAVOUR</div>
      <div class="title-whey">WHEY</div>
      <div class="title-protein">PROTEIN</div>
    </div>

    <div class="view-window"></div>

    <div class="benefits">
      <div class="benefit">PROBIOTICS<br>VITAMIN D</div>
      <div class="benefit">5.9G OF BCAAS<br>GLUTEN FREE</div>
      <div class="benefit">BANNED<br>SUBSTANCE FREE</div>
    </div>
    <div class="benefit-rule"></div>
    <div class="net-contents">2.51 KG/ 33 SERVES/ DIETARY SUPPLEMENT</div>

    <div class="base-band"></div>
  </main>
</body>
</html>
```